Design cover Book of special needs

The book talks about how the handicapped is given hope and happiness
Pictures of the disabled: Pictures must be expressive - Images should be about UAE or Gulf people (preferably UAE). Images may be referring to the disabled person - or a drawing or something
The book's cover should be a sign of happiness and light
Background: Must be attractive ...
Colors are dynamic colors and activity
Arabic Book Title
رحلة الضياء عبر المدى الواسع

تأليف
الدكتور هلال بن سالم المرزوقي
logo of Publishing
as attached
final the year
1440 - 2018

Size of cover is : 20cm x 20cm

Colors

Designer to choose colors to be used in the design.

Requirements
Must have
• The book talks about how the handicapped is given hope and happiness
• Pictures of the disabled: Pictures must be expressive - Images should be about UAE or Gulf people (preferably UAE). Images may be referring to the disabled person - or a drawing or something
• The book's cover should be a sign of happiness and light
• Background: Must be attractive ...
• Colors are dynamic colors and activity
Nice to have
• The image and background are spoken and expressive
• You Can change the color of logo to be suitable with the cover
Should not have
• Do not include photos of famous people

```html
<!DOCTYPE html>
<html lang="ar" dir="rtl">
<head>
<meta charset="utf-8">
<title>رحلة الضياء عبر المدى الواسع</title>
<link rel="stylesheet" href="https://fonts.googleapis.com/css2?family=Cairo:wght@400;700;900&display=swap">
<style>
  :root {
    --stage: #d9dadb;
    --paper: #fbf8f3;
    --warm-deep: #a8684b;
    --warm-mid: #d9a183;
    --warm-light: #f4dccb;
    --glow: #fff8ea;
    --sky: #b9dbe2;
    --title-red: #e4141b;
    --title-blue: #1a8fd6;
    --ink: #222222;
    --muted: #555555;
  }
  html, body {
    margin: 0;
    width: 1200px;
    height: 900px;
    overflow: hidden;
    background: var(--stage);
    font-family: "Cairo", sans-serif;
  }
  .book-cover {
    position: absolute;
    left: 210px;
    top: 60px;
    width: 780px;
    height: 780px;
    overflow: hidden;
    box-shadow: 0 12px 30px rgba(0,0,0,0.18);
    background:
      radial-gradient(ellipse at 72% 45%, var(--glow) 0%, rgba(255,248,234,0) 50%),
      linear-gradient(180deg, var(--paper) 0%, var(--warm-light) 55%, var(--sky) 100%);
  }
  .cover-photo {
    position: absolute;
    left: 0;
    top: 190px;
    width: 500px;
    height: 590px;
    background:
      linear-gradient(90deg, rgba(168,104,75,0) 70%, var(--warm-light) 100%),
      linear-gradient(0deg, rgba(244,220,203,0) 80%, var(--warm-light) 100%),
      linear-gradient(160deg, var(--warm-mid) 0%, var(--warm-deep) 60%, #8f563d 100%);
  }
  .series-label {
    position: absolute;
    top: 24px;
    left: 30px;
    font-size: 13px;
    font-weight: 700;
    color: var(--muted);
  }
  .publisher {
    position: absolute;
    top: 20px;
    right: 28px;
    display: flex;
    align-items: center;
    gap: 8px;
    font-size: 15px;
    font-weight: 700;
    color: var(--warm-deep);
  }
  .publisher-mark {
    width: 26px;
    height: 26px;
    background: var(--warm-deep);
  }
  .title-block {
    position: absolute;
    top: 70px;
    right: 130px;
    text-align: right;
  }
  .title-main {
    margin: 0;
    font-size: 76px;
    font-weight: 900;
    line-height: 1.1;
    color: var(--title-red);
  }
  .title-sub {
    margin: 0;
    font-size: 38px;
    font-weight: 700;
    line-height: 1.2;
    color: var(--title-blue);
  }
  .author-block {
    position: absolute;
    bottom: 34px;
    right: 330px;
    text-align: right;
  }
  .author-label {
    font-size: 28px;
    font-weight: 900;
    color: var(--ink);
    line-height: 1.2;
  }
  .author-name {
    font-size: 26px;
    font-weight: 700;
    color: var(--title-blue);
    line-height: 1.3;
    white-space: nowrap;
  }
  .edition-year {
    position: absolute;
    top: 210px;
    left: 30px;
    font-size: 17px;
    font-weight: 700;
    color: var(--paper);
    direction: ltr;
  }
</style>
</head>
<body>
  <main class="book-cover">
    <div class="cover-photo" role="img" aria-label="صورة رجل إماراتي بالزي التقليدي يجلس على كرسي متحرك في غرفة مضيئة بنور الشمس"></div>

    <div class="series-label">سلسلة الإصدارات ( 29 )</div>

    <div class="publisher">
      <span class="publisher-mark"></span>
      <span class="publisher-name">دار الأفق للنشر والتوزيع</span>
    </div>

    <header class="title-block">
      <h1 class="title-main">رحلة الضياء</h1>
      <p class="title-sub">عبر المدى الواسع</p>
    </header>

    <div class="edition-year">2018 - 1440هـ</div>

    <div class="author-block">
      <div class="author-label">تأليف</div>
      <div class="author-name">دكتور هلال بن سالم المرزوقي</div>
    </div>
  </main>
</body>
</html>
```